VELMARA Program Cover

Every year, we host an annual conference for educators who teach in afterschool in the Southwest. This year, we are renaming the conference to VELMARA 2014 (stands for Beyond-Classroom-Hours Pathways Summit). The theme of our conference is made up of three verbs: Innovate, Collaborate, & Thrive. We are looking for a program cover that is creative and yet visually appealing to an audience that ranges from Millennials to Baby Boomers. It needs to convey the three verbs and also brand the conference with the new name. We like the colors Blue and Green as our previous programs have been red, gold, yellow, and orange. Our audience teaches kids from K - 12, but likes to be treated as professionals (not the typical school clipart stuff). The conference is hosted at the Ft. Worth Calloway Lodge from July 23rd to July 24th, 2014. The program cover will set the tone for all conference materials (i.e. color scene, potential logo, etc...).

Target Market(s)

The target audience is participants of the conference. The age ranges from 25 to 60, but they are all either teachers, social workers, or educational administrators. All have a Bachelor's Degree or higher. While they are professionals, they also like to have fun.

Industry/Entity Type

Graphic Design

Requirements
Must have
• VELMARA must be prevalent and tagged with Beyond-Classroom-Hours Pathways Summit so that people know what it stands for.
Should not have
• The design should be clean with zero clipart.

```html
<!DOCTYPE html>
<html lang="en">
<head>
<meta charset="utf-8">
<title>VELMARA Program Cover</title>
<link rel="stylesheet" href="https://fonts.googleapis.com/css2?family=Russo+One&family=Montserrat:ital,wght@1,500&family=Kaushan+Script&family=Black+Ops+One&display=swap">
<style>
  :root {
    --bg-top: #dcd4dc;
    --bg-mid: #c4bfdc;
    --bg-bottom: #aaa8d6;
    --brand-silver-light: #a4a4b0;
    --brand-silver-dark: #5e5e6c;
    --navy: #1c1f78;
    --blue: #0a1cf0;
    --green: #5cb30c;
    --green-dark: #2f8a1c;
    --ink: #161616;
    --photo-warm: #c9a79a;
    --photo-cool: #8f95b8;
    --ornament: #4a4a58;
  }
  html, body {
    margin: 0;
    padding: 0;
    width: 927px;
    height: 1200px;
    overflow: hidden;
    background: var(--bg-bottom);
  }
  .cover {
    display: block;
    width: 927px;
    height: 1200px;
  }
  .brand-name {
    font-family: "Russo One", sans-serif;
    fill: url(#brand-silver);
  }
  .tagline {
    font-family: "Montserrat", sans-serif;
    font-style: italic;
    font-weight: 500;
    fill: var(--navy);
  }
  .venue-line {
    font-family: "Kaushan Script", cursive;
    fill: var(--ink);
  }
  .year {
    font-family: "Russo One", sans-serif;
  }
  .year-green { fill: var(--green-dark); }
  .year-blue { fill: var(--blue); }
  .theme {
    font-family: "Black Ops One", sans-serif;
    fill: var(--ink);
    letter-spacing: 0.5px;
  }
</style>
</head>
<body>
<svg class="cover" viewBox="0 0 612 792" preserveAspectRatio="none" xmlns="http://www.w3.org/2000/svg">
  <defs>
    <linearGradient id="backdrop" x1="0" y1="0" x2="0" y2="1">
      <stop offset="0" stop-color="var(--bg-top)"/>
      <stop offset="0.45" stop-color="var(--bg-mid)"/>
      <stop offset="1" stop-color="var(--bg-bottom)"/>
    </linearGradient>
    <linearGradient id="light-beam" x1="1" y1="0" x2="0" y2="1">
      <stop offset="0" stop-color="#ffffff" stop-opacity="0.55"/>
      <stop offset="1" stop-color="#ffffff" stop-opacity="0"/>
    </linearGradient>
    <linearGradient id="brand-silver" x1="0" y1="0" x2="0" y2="1">
      <stop offset="0" stop-color="var(--brand-silver-light)"/>
      <stop offset="1" stop-color="var(--brand-silver-dark)"/>
    </linearGradient>
    <linearGradient id="photo-group-top" x1="0" y1="0" x2="1" y2="1">
      <stop offset="0" stop-color="var(--photo-warm)"/>
      <stop offset="1" stop-color="var(--photo-cool)"/>
    </linearGradient>
    <linearGradient id="photo-group-right" x1="0" y1="0" x2="1" y2="1">
      <stop offset="0" stop-color="var(--photo-cool)"/>
      <stop offset="1" stop-color="var(--photo-warm)"/>
    </linearGradient>
  </defs>

  <!-- backdrop -->
  <rect class="backdrop" width="612" height="792" fill="url(#backdrop)"/>
  <polygon class="backdrop-beam" points="612,120 612,300 0,560 0,420" fill="url(#light-beam)"/>

  <!-- brand block -->
  <g class="brand">
    <text class="brand-name" x="86" y="256" font-size="124" textLength="434" lengthAdjust="spacingAndGlyphs">VELMARA</text>
    <rect class="photo-group photo-group-top" x="160" y="104" width="85" height="46" rx="6" fill="url(#photo-group-top)" role="img" aria-label="Photo of children playing with colourful scarves"/>
    <rect class="photo-group photo-group-right" x="528" y="204" width="76" height="70" rx="6" fill="url(#photo-group-right)" role="img" aria-label="Photo of a group of children sitting together"/>
    <text class="tagline" x="68" y="290" font-size="23" textLength="490" lengthAdjust="spacingAndGlyphs">Beyond-Classroom-Hours Pathways Summit</text>
  </g>

  <!-- vertical bars -->
  <g class="bars">
    <rect x="285" y="312" width="1.6" height="208" fill="var(--green)"/>
    <rect x="290" y="304" width="2" height="216" fill="var(--green)"/>
    <rect x="296" y="298" width="6" height="222" fill="var(--green)"/>
    <rect x="308" y="298" width="7" height="222" fill="var(--blue)"/>
    <rect x="318" y="304" width="2" height="216" fill="var(--blue)"/>
    <rect x="324" y="312" width="1.6" height="208" fill="var(--blue)"/>
  </g>

  <!-- event details -->
  <text class="venue-line" x="168" y="545" font-size="15.5" textLength="367" lengthAdjust="spacingAndGlyphs">Ft. Worth Calloway Lodge from July 23rd to July 24th, 2014</text>
  <text class="year" x="243" y="588" font-size="42" textLength="127" lengthAdjust="spacingAndGlyphs"><tspan class="year-green">20</tspan><tspan class="year-blue">14</tspan></text>
  <rect class="ornament" x="262" y="594" width="90" height="16" rx="7" fill="var(--ornament)" opacity="0.35" role="img" aria-label="Decorative flourish divider"/>

  <!-- waves -->
  <path class="wave wave-green" d="M0,612 C150,604 260,636 380,658 C470,672 540,636 612,614 L612,668 C560,690 480,716 380,706 C260,692 150,652 0,656 Z" fill="var(--green)"/>
  <path class="wave wave-blue" d="M0,578 C150,572 260,610 360,634 C430,650 510,606 612,586 L612,620 C540,642 470,674 380,662 C260,640 150,610 0,616 Z" fill="var(--blue)"/>

  <!-- theme -->
  <text class="theme" x="168" y="760" font-size="17.5" textLength="308" lengthAdjust="spacingAndGlyphs">INNOVATE, COLLABORATE, &amp; THRIVE</text>
</svg>
</body>
</html>
```